I need a business card that is professional /minimalistic ( clean edges) to help develop my new business venture that is car valeting / detailing.

I would like to use a black background, white font,red car silhouette above the text.

have now added phone numbers thanks

Industry/Entity Type

Business

Contact Information for Business Card

Gleamcraft Studio,
Valeting & Detailing Specialist,
tel 01638 219054 mob 07814 605193, Dean Marlowe, 7 Hawthorn Rise. East Brackley, Thornmere. IP19 3JD

```html
<!DOCTYPE html>
<html lang="en">
<head>
<meta charset="utf-8">
<title>Gleamcraft Studio – Business Card</title>
<link rel="stylesheet" href="https://fonts.googleapis.com/css2?family=Oswald:wght@600&family=Open+Sans:wght@300;400;600&display=swap">
<style>
  :root {
    --backdrop: #b4b4b4;
    --card-dark: #262626;
    --card-mid: #303030;
    --card-band: #3a3a3a;
    --stripe-light: #e6e6e6;
    --stripe-grey: #a9a9a9;
    --accent-green: #9fd11b;
    --text-white: #ffffff;
    --text-soft: #e2e2e2;
  }
  * { margin: 0; padding: 0; box-sizing: border-box; }
  html, body {
    width: 1200px;
    height: 900px;
    overflow: hidden;
    background: var(--backdrop);
  }
  .business-card {
    position: absolute;
    left: 110px;
    top: 170px;
    width: 980px;
    height: 560px;
    background: var(--card-dark);
    overflow: hidden;
    font-family: "Open Sans", Arial, sans-serif;
    color: var(--text-white);
    box-shadow: 0 6px 18px rgba(0,0,0,0.25);
  }
  .identity-band {
    position: absolute;
    left: 0; top: 255px;
    width: 100%; height: 130px;
    background: var(--card-mid);
  }
  .address-band {
    position: absolute;
    left: 0; top: 385px;
    width: 100%; height: 78px;
    background: var(--card-band);
  }
  .divider-stripes {
    position: absolute;
    left: 0; top: 463px;
    width: 100%; height: 17px;
    background: linear-gradient(to bottom,
      var(--stripe-grey) 0 4px,
      var(--stripe-light) 4px 8px,
      var(--stripe-grey) 8px 11px,
      var(--stripe-light) 11px 17px);
  }
  .footer-band {
    position: absolute;
    left: 0; top: 480px;
    width: 100%; height: 80px;
    background: var(--accent-green);
  }
  .person {
    position: absolute;
    right: 110px;
    top: 92px;
    text-align: right;
  }
  .person-name {
    font-weight: 300;
    font-size: 36px;
    letter-spacing: -1px;
    line-height: 1;
  }
  .person-role {
    font-size: 17px;
    color: var(--accent-green);
    line-height: 1.3;
  }
  .brand-mark {
    position: absolute;
    left: 78px; top: 286px;
    width: 88px; height: 88px;
    border-radius: 12px;
    background: var(--accent-green);
  }
  .brand-name {
    position: absolute;
    left: 196px; top: 266px;
    font-family: "Oswald", "Arial Narrow", sans-serif;
    font-weight: 600;
    font-size: 40px;
    line-height: 1.2;
    color: var(--text-white);
    text-transform: uppercase;
  }
  .brand-tagline {
    position: absolute;
    left: 198px; top: 318px;
    font-weight: 600;
    font-size: 18px;
    letter-spacing: 0.6px;
    color: var(--text-soft);
  }
  .contact-line {
    position: absolute;
    display: flex;
    align-items: center;
    gap: 12px;
    font-size: 18px;
    color: var(--text-soft);
  }
  .contact-tel { left: 540px; top: 340px; }
  .contact-mob { left: 740px; top: 340px; }
  .contact-address {
    left: 128px; top: 396px;
    align-items: flex-start;
    line-height: 28px;
  }
  .contact-address address { font-style: normal; }
  .contact-icon { flex: none; fill: var(--accent-green); }
  .pin-icon { margin-top: 4px; }
</style>
</head>
<body>
  <div class="business-card">
    <div class="identity-band"></div>
    <div class="address-band"></div>
    <div class="divider-stripes"></div>
    <div class="footer-band"></div>

    <div class="person">
      <div class="person-name">YOUR NAME</div>
      <div class="person-role">Position</div>
    </div>

    <div class="brand-mark"></div>
    <div class="brand-name">Gleamcraft Studio</div>
    <div class="brand-tagline">Valeting &amp; Detailing Specialist</div>

    <div class="contact-line contact-tel">
      <svg class="contact-icon" width="14" height="18" viewBox="0 0 14 18" aria-hidden="true">
        <path d="M3 1h3l1 4-2 1.5c.8 2.4 2 4 3.6 5.5L10.5 10l3.5 1.5V15c0 1-1 2-2 2C6 16.5 1 11 1 3c0-1 1-2 2-2z"/>
      </svg>
      <span>+(01638) 219-054</span>
    </div>

    <div class="contact-line contact-mob">
      <svg class="contact-icon" width="12" height="20" viewBox="0 0 12 20" aria-hidden="true">
        <path d="M2 0h8a2 2 0 0 1 2 2v16a2 2 0 0 1-2 2H2a2 2 0 0 1-2-2V2a2 2 0 0 1 2-2zm0 3v10h8V3zm4 12a1.4 1.4 0 1 0 0 2.8A1.4 1.4 0 0 0 6 15z"/>
      </svg>
      <span>+(07814) 605-193</span>
    </div>

    <div class="contact-line contact-address">
      <svg class="contact-icon pin-icon" width="14" height="20" viewBox="0 0 14 20" aria-hidden="true">
        <path d="M7 0a7 7 0 0 1 7 7c0 5-7 13-7 13S0 12 0 7a7 7 0 0 1 7-7zm0 4a3 3 0 1 0 0 6 3 3 0 0 0 0-6z"/>
      </svg>
      <address>
        Dean Marlowe, 7 Hawthorn Rise.<br>
        East Brackley, Thornmere. IP19 3JD
      </address>
    </div>
  </div>
</body>
</html>
```